Bellmoor Commercial Finance Information Brochure

This brochure will be sent out to clients via A4 PDF on an email to showcase what our company has to offer. We are a commercial finance brokerage, that specialises in property finance. We would like to see designs following our colour scheme. The final design should demonstrate our professionalism and reliability.
I have attached our logo and also a few bullet points on our information and what we can offer. These can be slightly reworded for conciseness. Or leave the text sections as filler and I can fill these in.
I have also attached an overview of our colour scheme and design styling for your consideration.
Target Market(s)
Property Developers
Industry/Entity Type
Financial Services

```html
<!DOCTYPE html>
<html lang="en">
<head>
<meta charset="utf-8">
<title>Bellmoor Finance – Information Brochure</title>
<link href="https://fonts.googleapis.com/css2?family=Figtree:wght@400;600;700&display=swap" rel="stylesheet">
<style>
  :root {
    --brand-blue: #1c3f94;
    --brand-green: #2a8a3a;
    --ink: #1f1f24;
    --white: #ffffff;
    --photo-top: #dfe6ee;
    --photo-mid: #7f93a8;
    --photo-low: #3b536e;
  }
  * { margin: 0; padding: 0; box-sizing: border-box; }
  html, body { width: 848px; height: 1200px; overflow: hidden; background: var(--white); }
  body { font-family: "Figtree", sans-serif; color: var(--brand-blue); }
  .brochure { position: relative; width: 848px; height: 1200px; overflow: hidden; background: var(--white); }

  .top-band { position: absolute; left: 0; top: 0; width: 848px; height: 34px; background: var(--brand-blue); }

  .brand-name {
    position: absolute; left: 150px; top: 51px; width: 263px; height: 76px;
    display: flex; align-items: center; justify-content: center;
    font-weight: 700; font-size: 27px; letter-spacing: 1px; color: var(--brand-blue);
  }

  .intro { position: absolute; left: 51px; top: 164px; width: 462px; }
  .intro-heading { font-size: 21px; line-height: 25.6px; font-weight: 700; margin-bottom: 16px; }
  .intro-text { font-size: 14px; line-height: 18px; font-weight: 400; margin-bottom: 9px; }
  .intro-lead { font-size: 14.5px; line-height: 19px; font-weight: 700; margin-bottom: 9px; }

  .features { position: absolute; left: 51px; top: 486px; width: 460px; }
  .feature { position: absolute; left: 0; width: 460px; }
  .feature-icon { position: absolute; left: 0; width: 82px; height: 82px; border-radius: 50%; background: var(--brand-blue); }
  .feature-icon svg { width: 82px; height: 82px; }
  .feature-body { position: absolute; left: 101px; width: 345px; }
  .feature-title { font-size: 16px; font-weight: 700; color: var(--brand-green); line-height: 20px; }
  .feature-text { font-size: 13.6px; line-height: 18px; color: var(--ink); }

  .photo {
    position: absolute; left: 540px; top: 34px; width: 256px; height: 351px;
    background: linear-gradient(175deg, var(--photo-top) 0%, var(--photo-mid) 45%, var(--photo-low) 100%);
  }
  .efficiency-panel {
    position: absolute; left: 540px; top: 385px; width: 256px; height: 580px;
    background: var(--brand-blue); border-radius: 0 0 18px 18px; color: var(--white); text-align: center;
  }
  .panel-heading { position: absolute; left: 12px; top: 26px; width: 232px; font-size: 22px; line-height: 29px; font-weight: 700; }
  .panel-text { position: absolute; left: 14px; top: 248px; width: 228px; font-size: 14px; line-height: 18px; font-weight: 600; }
  .panel-icon { position: absolute; left: 68px; top: 393px; width: 120px; height: 165px; }

  .tagline { position: absolute; left: 0; top: 1018px; width: 848px; text-align: center; font-size: 15.5px; line-height: 21px; font-weight: 700; }

  .footer-wave { position: absolute; left: 0; top: 1050px; width: 848px; height: 150px; }
  .contact { position: absolute; top: 1138px; color: var(--white); font-size: 13px; line-height: 20px; }
  .contact-address { left: 60px; width: 220px; text-align: center; }
  .contact-phone { left: 360px; width: 140px; }
  .contact-web { left: 585px; width: 200px; }
  .contact-line { display: flex; align-items: center; gap: 6px; }
  .contact-line svg { width: 12px; height: 12px; flex: none; }
  .divider { position: absolute; top: 1141px; width: 2px; height: 35px; background: var(--white); }
</style>
</head>
<body>
<div class="brochure">
  <div class="top-band"></div>

  <div class="brand-name">BELLMOOR FINANCE</div>

  <section class="intro">
    <h1 class="intro-heading">As former lenders and developers ourselves, we intimately understand the inefficiencies that plague deals in the market today.</h1>
    <p class="intro-text">We’ve experienced the frustration of tight time limits on deals and the exasperation of brokers wasting precious time collecting information. It’s enough to drive developers and lenders insane!</p>
    <p class="intro-lead">That’s why we founded Bellmoor Finance – the efficient and reliable link connecting developers and lenders.</p>
    <p class="intro-text">Our streamlined processes eliminate unnecessary hurdles, enabling clear and swift communication throughout.<br>No more wasted time. No more unnecessary stress.</p>
  </section>

  <section class="features">
    <div class="feature" style="top:0">
      <div class="feature-icon" style="top:0">
        <svg viewBox="0 0 82 82" fill="none" stroke="#fff" stroke-width="2.4" stroke-linecap="round" stroke-linejoin="round">
          <circle cx="44" cy="32" r="11"/><circle cx="44" cy="32" r="6"/>
          <path d="M44 17v3M44 44v3M29 32h3M56 32h3M33 21l2 2M53 41l2 2M33 43l2-2M53 23l2-2"/>
          <path d="M20 58l6-8h10l8 3h6"/><path d="M26 50l10 8 22-9"/><path d="M18 52l5 10"/>
        </svg>
      </div>
      <div class="feature-body" style="top:2px">
        <h2 class="feature-title">OUR APPROACH</h2>
        <p class="feature-text">With our expertise and industry insights, we’ve developed a unique approach that simplifies the commercial financing journey, guiding you every step of the way.</p>
      </div>
    </div>
    <div class="feature" style="top:132px">
      <div class="feature-icon" style="top:0">
        <svg viewBox="0 0 82 82" fill="none" stroke="#fff" stroke-width="2.4" stroke-linecap="round" stroke-linejoin="round">
          <path d="M22 44a19 19 0 0 1 38 0"/><path d="M41 22v4M26 30l3 3M56 30l-3 3M20 44h4M58 44h4"/>
          <path d="M36 38h10l-2 4c7 3 9 8 8 13H30c-1-5 1-10 8-13z" fill="#fff"/>
        </svg>
      </div>
      <div class="feature-body" style="top:-6px">
        <h2 class="feature-title">OUR EXPERIENCE</h2>
        <p class="feature-text">With our background in the asset management industry, we have cultivated a black book of fund managers, institutions, UHNWI and private equity lenders we can call on for non-traditional lending.</p>
      </div>
    </div>
    <div class="feature" style="top:253px">
      <div class="feature-icon" style="top:0">
        <svg viewBox="0 0 82 82" fill="none" stroke="#fff" stroke-width="2.4" stroke-linecap="round" stroke-linejoin="round">
          <circle cx="47" cy="44" r="15"/><circle cx="47" cy="44" r="10" stroke-dasharray="2 3"/>
          <path d="M47 44l5-5M44 26h6M47 26v3M60 30l3-3"/><path d="M14 38h14M17 44h11M20 50h8"/>
        </svg>
      </div>
      <div class="feature-body" style="top:-6px">
        <h2 class="feature-title">OUR PROCESS</h2>
        <p class="feature-text">By employing cutting-edge technology and streamlining our internal processes, we have cultivated a seamless and time-saving approach to finance brokering.</p>
      </div>
    </div>
    <div class="feature" style="top:373px">
      <div class="feature-icon" style="top:0">
        <svg viewBox="0 0 82 82" fill="none" stroke="#fff" stroke-width="2.4" stroke-linecap="round" stroke-linejoin="round">
          <rect x="27" y="22" width="30" height="38" rx="2"/><rect x="36" y="19" width="12" height="6" rx="1"/>
          <path d="M32 32l2 2 3-3M40 33h12M32 41l2 2 3-3M40 42h12M32 50h6"/>
          <path d="M20 30l10 16"/><circle cx="54" cy="52" r="4" fill="#fff"/><path d="M46 62a8 6 0 0 1 16 0z" fill="#fff"/>
        </svg>
      </div>
      <div class="feature-body" style="top:-6px">
        <h2 class="feature-title">OUR ADVANTAGE</h2>
        <p class="feature-text">We are well-versed in the questions lenders will ask, allowing us to get ahead of the curve and request all the necessary information from you on day one – giving you a distinct advantage.</p>
      </div>
    </div>
  </section>

  <div class="photo" role="img" aria-label="Photograph looking up at glass office towers against a pale sky"></div>

  <aside class="efficiency-panel">
    <h2 class="panel-heading">Bellmoor Finance was created to satisfy a need in the market that has been far too overlooked – efficiency.</h2>
    <p class="panel-text">Efficiency is at the heart of our operations, and we pride ourselves on our ability to secure the best financing options swiftly and effectively for our clients.</p>
    <svg class="panel-icon" viewBox="0 0 120 165" fill="none" stroke="#fff" stroke-width="3" stroke-linejoin="round" stroke-linecap="round">
      <path d="M60 2l-20 22h12v32h16V24h12z" fill="#fff" stroke="none"/>
      <path d="M19 30L1 52h11v26h14V52h11z" fill="#fff" stroke="none"/>
      <path d="M99 16L81 38h11v40h14V38h11z" fill="#fff" stroke="none"/>
      <path d="M20 90a50 50 0 0 0 78 60"/><path d="M104 104a50 50 0 0 0-12-22"/>
      <path d="M92 150l8-2-2 8"/><path d="M22 84l-4 8 8 1"/>
      <circle cx="60" cy="112" r="22" fill="#fff" stroke="none"/>
      <path d="M60 84v8M60 132v8M32 112h8M80 112h8M40 92l5 5M75 127l5 5M40 132l5-5M75 97l5-5" stroke-width="8"/>
      <circle cx="60" cy="112" r="14" stroke="#1c3f94" stroke-width="2.5"/>
      <path d="M53 112l5 5 9-9" stroke="#1c3f94" stroke-width="2.5"/>
    </svg>
  </aside>

  <p class="tagline">By entrusting us with this responsibility, you can focus on your core tasks<br>and leave the financing aspect to us, making the process less stressful for you.</p>

  <svg class="footer-wave" viewBox="0 0 848 150" preserveAspectRatio="none">
    <path d="M0 39 Q 420 72 848 28 L848 150 L0 150 Z" fill="#1c3f94"/>
    <path d="M37 37 Q 420 70 848 16 L848 30 Q 420 80 37 37 Z" fill="#2a8a3a"/>
  </svg>

  <div class="contact contact-address">1420 Harbor Ridge Road,<br>Fairhaven, Oregon 97410</div>
  <div class="divider" style="left:317px"></div>
  <div class="contact contact-phone">
    <div class="contact-line"><svg viewBox="0 0 12 12"><path d="M2 1l2 0 1 3-1.5 1a7 7 0 0 0 3.5 3.5L8 7l3 1v2a1 1 0 0 1-1 1A9 9 0 0 1 1 2a1 1 0 0 1 1-1z" fill="#fff"/></svg>555-214-7730</div>
    <div class="contact-line"><svg viewBox="0 0 12 12"><rect x="3" y="0.5" width="6" height="11" rx="1" fill="none" stroke="#fff" stroke-width="1.2"/><circle cx="6" cy="9.5" r="0.8" fill="#fff"/></svg>555-214-7781</div>
  </div>
  <div class="divider" style="left:531px"></div>
  <div class="contact contact-web">
    <div class="contact-line"><svg viewBox="0 0 12 12"><rect x="0.5" y="2" width="11" height="8" fill="#fff"/><path d="M0.5 2l5.5 4.5L11.5 2" fill="none" stroke="#1c3f94" stroke-width="1"/></svg>hello@bellmoorfinance.com</div>
    <div class="contact-line"><svg viewBox="0 0 12 12"><circle cx="6" cy="6" r="5.3" fill="none" stroke="#fff" stroke-width="1.2"/><path d="M1 6h10M6 0.7c-3 3-3 7.6 0 10.6M6 0.7c3 3 3 7.6 0 10.6" fill="none" stroke="#fff" stroke-width="1"/></svg>www.bellmoorfinance.com</div>
  </div>
</div>
</body>
</html>
```